Create a memorable Web Design for real estate branding

we are a Minnepolis brokerage and boutique housing specialist with over 27 years of experience in the Global furnished housing industry, servicing the Greater Los Angeles area. Specializing in “warm environments” we offer a customized approach to satisfying our guests and client’s needs by offering a wide array of options in highly desirable areas. Additionally, Lanterly Homes Collective offers assistance and expertise to home buyers, sellers and investors.

Industry/Entity Type

Real Estate

Number of Pages Required

1 page

Font styles to use
Serif
Sans Serif
Decorative

```html
<!DOCTYPE html>
<html lang="en">
<head>
<meta charset="utf-8">
<title>Lanterly Homes Collective</title>
<link rel="stylesheet" href="https://fonts.googleapis.com/css2?family=Cinzel:wght@400;700&family=Raleway:wght@400;500;600;700&display=swap">
<style>
:root{
  --teal:#16a68f;
  --teal-dark:#0f8d79;
  --green:#3db34a;
  --ink:#2b2b2b;
  --text:#3a3a3a;
  --muted:#666;
  --bar:#333333;
  --footer:#343434;
  --footer-deep:#272727;
  --line:#dcdcdc;
  --pale:#eef3e3;
  --white:#fff;
}
*{box-sizing:border-box;margin:0;padding:0}
html,body{width:1200px;height:3197px;overflow:hidden}
body{font-family:"Raleway",sans-serif;color:var(--text);background:var(--white);font-size:14px}
.container{width:1040px;margin:0 auto;position:relative}

/* top bar */
.topbar{height:30px;background:var(--bar);color:#ddd;font-size:12.5px}
.topbar .container{height:100%;display:flex;align-items:center;justify-content:space-between}
.topbar .contact{display:flex;gap:22px;align-items:center}
.topbar .contact span{display:flex;align-items:center;gap:6px}
.topbar .dot{width:12px;height:12px;border-radius:50%;background:var(--green);display:inline-block}
.topbar .right{display:flex;height:100%;align-items:stretch;margin-right:-20px}
.topbar .area{background:var(--green);color:#1d3a12;font-family:"Cinzel",serif;font-size:12px;display:flex;align-items:center;padding:0 14px;font-weight:700;white-space:nowrap}
.topbar .social{width:32px;border-left:1px solid #555;display:flex;align-items:center;justify-content:center}
.topbar .social i{width:10px;height:10px;background:#bbb;display:block}

/* header */
.header{height:136px;background:var(--white)}
.header .container{height:100%}
.logo{position:absolute;left:0;top:30px;width:310px;height:80px;display:flex;flex-direction:column;align-items:center;color:var(--green);font-weight:700;white-space:nowrap}
.logo .name{font-size:34px;line-height:42px;letter-spacing:1px}
.logo .sub{font-size:24px;line-height:30px;letter-spacing:3px}
.cta{position:absolute;right:0;top:25px;width:277px;height:47px;background:var(--teal);color:var(--white);font-family:"Cinzel",serif;font-size:16px;display:flex;align-items:center;justify-content:center;font-weight:700;white-space:nowrap}
.nav{position:absolute;right:0;top:97px;display:flex;font-family:"Cinzel",serif;font-size:15px;color:var(--ink);white-space:nowrap}
.nav a{padding:0 14px;border-left:1px solid #999;line-height:16px;text-decoration:none;color:inherit}
.nav a:first-child{border:0;color:var(--teal)}
.nav a:last-child{padding-right:0}

/* hero */
.hero{height:512px;position:relative;background:linear-gradient(180deg,#5d86b3 0%,#a8bfd5 30%,#6c6b68 55%,#3f4a33 80%,#2e3a24 100%)}
.hero .title{position:absolute;top:197px;width:100%;text-align:center;color:var(--white);font-family:"Cinzel",serif;font-size:38px;letter-spacing:1px}
.hero .btn{position:absolute;left:522px;top:292px;width:156px;height:47px;border:2px solid var(--white);color:var(--white);display:flex;align-items:center;justify-content:center;font-size:17px;font-weight:500}
.arrows{position:absolute;display:flex;gap:8px}
.arrows span{width:28px;height:28px;border-radius:50%;display:flex;align-items:center;justify-content:center}
.hero .arrows{left:566px;top:446px}
.hero .arrows span:first-child{background:var(--white)}
.hero .arrows span:last-child{background:var(--teal)}

/* welcome */
.welcome{height:647px;background:linear-gradient(135deg,#f7f7f7,#ececec 50%,#f7f7f7)}
.section-title{text-align:center;font-family:"Cinzel",serif;color:var(--ink);font-size:30px;letter-spacing:1px;white-space:nowrap}
.welcome .section-title{padding-top:36px;display:flex;justify-content:center;align-items:baseline;gap:14px}
.welcome .section-title .brand{color:var(--green);font-family:"Raleway",sans-serif;font-weight:700;font-size:28px}
.rule{width:320px;height:1px;background:#bbb;margin:8px auto 0}
.welcome .intro{margin-top:34px;font-size:13.5px;line-height:21px;text-align:center;color:var(--text)}
.offers{display:flex;justify-content:space-between;width:900px;margin:46px auto 0}
.offer{width:397px;text-align:center}
.offer .photo{height:264px}
.offer h3{margin-top:18px;font-size:19px;font-weight:500;letter-spacing:1px;color:var(--ink)}
.offer p{margin-top:8px;font-size:13.5px;line-height:21px}

/* reviews */
.reviews{height:363px;position:relative;background:linear-gradient(180deg,#3a4556,#2c3643 60%,#263022)}
.reviews .section-title{color:var(--white);padding-top:50px}
.reviews .rule{background:#aaa}
.avatar{position:absolute;left:179px;top:152px;width:110px;height:110px;border-radius:50%;border:4px solid var(--white);background:#c7b7a4}
.quote{position:absolute;left:309px;top:148px;width:710px;color:var(--white);font-style:italic;font-size:12.5px;line-height:23px}
.quote .mark{position:absolute;left:0;top:-6px;font-size:30px;line-height:30px;color:#ccc;font-style:normal}
.quote p{padding-left:32px}
.quote .by{margin-top:6px;font-weight:700}
.reviews .arrows{left:582px;top:302px;gap:4px}
.reviews .arrows span{border-radius:0;width:22px;height:22px;background:#556}
.reviews .arrows span:last-child{background:var(--teal)}

/* why */
.why{height:490px;background:linear-gradient(135deg,var(--pale),#f7f9f1 50%,#e6eed3)}
.why .section-title{padding-top:46px;font-size:26px;font-weight:700}
.why .rule{width:200px}
.features{display:grid;grid-template-columns:repeat(3,340px);justify-content:center;row-gap:30px;margin-top:42px;margin-left:21px}
.feature{text-align:center}
.feature .icon{width:98px;height:98px;border-radius:50%;border:2px solid var(--ink);margin:0 auto;display:flex;align-items:center;justify-content:center;background:var(--white)}
.feature .icon.active{background:var(--teal);border-color:var(--teal)}
.feature h4{margin-top:22px;font-size:17px;font-weight:500;letter-spacing:.5px;color:var(--ink)}

/* listings */
.listings{height:477px;background:#f3f3f3}
.listings .section-title{padding-top:38px;font-size:28px;font-weight:700}
.listings .rule{width:280px}
.cards{display:flex;gap:30px;margin:40px 0 0 79px}
.card{width:238px;height:313px;background:var(--white);border:1px solid var(--line);padding:8px}
.card .photo{height:130px}
.card h5{margin-top:18px;font-size:14px;font-weight:600;color:var(--ink)}
.card .desc{margin-top:6px;font-size:12.5px;color:var(--muted)}
.card .row{display:flex;justify-content:space-between;align-items:center;margin-top:28px}
.tag{font-size:12px;color:var(--white);padding:4px 10px}
.tag.rent{background:var(--teal)}
.tag.sold{background:#333}
.price{color:var(--teal);font-size:22px}
.meta{display:flex;margin:14px -8px 0;border-top:1px solid var(--line);font-size:10px;color:#777}
.meta span{flex:1;text-align:center;padding-top:10px;border-left:1px solid var(--line)}
.meta span:first-child{border:0}

/* newsletter */
.newsletter{height:90px;background:var(--teal)}
.newsletter .container{height:100%;display:flex;align-items:center}
.newsletter .badge{width:46px;height:46px;border-radius:50%;background:#bfe6c9;border:3px solid var(--white);display:flex;align-items:center;justify-content:center;margin-left:12px;flex:none}
.newsletter h3{font-family:"Cinzel",serif;color:var(--white);font-size:27px;font-weight:400;margin-left:12px;letter-spacing:1px;white-space:nowrap}
.newsletter .chev{margin-left:10px;flex:none}
.newsletter .input{margin-left:24px;width:432px;height:45px;background:var(--white);font-size:13px;color:#888;padding:0 12px;display:flex;align-items:center;flex:none}
.newsletter .submit{margin-left:26px;width:149px;height:45px;background:#333;color:var(--white);font-size:22px;display:flex;align-items:center;justify-content:center;flex:none}

/* footer */
.footer{height:405px;background:var(--footer);color:#ddd}
.footer .cols{position:relative;height:100%}
.col{position:absolute;top:50px}
.col h4{font-family:"Cinzel",serif;font-size:19px;color:var(--white);font-weight:400;white-space:nowrap}
.col h4 em{font-style:normal;color:#9fcf6a}
.links{list-style:none;margin-top:26px;font-size:13px}
.links li{margin-bottom:25px}
.links li::before{content:"›";margin-right:10px}
.info{margin-top:24px;font-size:13.5px}
.info div{display:flex;align-items:center;gap:14px;margin-bottom:24px;line-height:20px}
.info i{width:30px;height:30px;background:var(--teal);display:flex;align-items:center;justify-content:center;flex:none}
.form{margin-top:22px;width:222px}
.form div{height:33px;background:var(--white);margin-bottom:9px;font-size:11px;color:#999;padding:9px 8px}
.form .msg{height:68px}
.form .send{width:152px;height:33px;background:var(--teal);color:var(--white);font-size:15px;font-weight:600;display:flex;align-items:center;justify-content:center}
.follow{margin-top:24px;font-size:12px;font-weight:500}
.follow div{display:flex;align-items:center;gap:16px;margin-bottom:13px}
.follow i{width:40px;height:40px;border-radius:50%;border:2px solid #555;display:block;background:var(--teal)}
.copy{height:47px;background:var(--footer-deep);color:#aaa;text-align:center;font-size:13px;line-height:47px}
</style>
</head>
<body>

<div class="topbar">
  <div class="container">
    <div class="contact">
      <span><i class="dot"></i>123-456-7890</span>
      <span><i class="dot"></i>hello@lanterlyhomes.com</span>
    </div>
    <div class="right">
      <div class="area">Servicing the Greater Los Angeles area</div>
      <div class="social"><i></i></div>
      <div class="social"><i></i></div>
      <div class="social"><i></i></div>
      <div class="social"><i></i></div>
    </div>
  </div>
</div>

<header class="header">
  <div class="container">
    <div class="logo"><span class="name">Lanterly Homes</span><span class="sub">Collective</span></div>
    <div class="cta">Schedule Free Consultation</div>
    <nav class="nav">
      <a>Find a Home</a><a>Sell Your Home</a><a>Hearthline Blog</a><a>Our Agents</a><a>Contact Us</a>
    </nav>
  </div>
</header>

<section class="hero" role="img" aria-label="City skyline of downtown towers above a green park">
  <h1 class="title">Boutique Brokerage</h1>
  <div class="btn">Get Started</div>
  <div class="arrows">
    <span><svg width="12" height="12" viewBox="0 0 12 12"><path d="M8 2 4 6l4 4" stroke="#333" stroke-width="2" fill="none"/></svg></span>
    <span><svg width="12" height="12" viewBox="0 0 12 12"><path d="M4 2l4 4-4 4" stroke="#fff" stroke-width="2" fill="none"/></svg></span>
  </div>
</section>

<section class="welcome">
  <h2 class="section-title">Welcome to <span class="brand">Lanterly Homes Collective</span></h2>
  <div class="rule" style="width:600px"></div>
  <div class="container">
    <p class="intro">Lorem ipsum dolor sit amet, consectetuer adipiscing elit, sed diam nonummy nibh euismod tincidunt ut laoreet dolore magna aliquam erat volutpat. Ut wisi enim ad minim veniam, quis nostrud exerci tation ullamcorper suscipit lobortis nisl ut aliquip ex ea commodo consequat. Duis autem vel eum iriure dolor in hendrerit in vulputate velit esse molestie consequat, vel illum dolore eu feugiat nulla facilisis at vero</p>
  </div>
  <div class="offers">
    <div class="offer">
      <div class="photo" role="img" aria-label="Modern living room with curved ceiling and lounge seating" style="background:linear-gradient(180deg,#c9b9a2,#8d6a4a 55%,#5a4534)"></div>
      <h3>BUY WITH US</h3>
      <p>Lorem ipsum dolor sit amet, consectetuer adipiscing elit, sed diam nonummy nibh euismod tincidunt ut laoreet dolore magna aliquam erat volutpat. Ut wisi enim ad minim veniam.</p>
    </div>
    <div class="offer">
      <div class="photo" role="img" aria-label="Couple shaking hands with an agent in front of a house" style="background:linear-gradient(180deg,#8fb0cf,#c9cfd2 40%,#5f7f4a 80%,#3f6030)"></div>
      <h3>SELL WITH US</h3>
      <p>Lorem ipsum dolor sit amet, consectetuer adipiscing elit, sed diam nonummy nibh euismod tincidunt ut laoreet dolore magna aliquam erat volutpat. Ut wisi enim ad minim veniam.</p>
    </div>
  </div>
</section>

<section class="reviews" role="img" aria-label="Dimmed city skyline behind customer reviews">
  <h2 class="section-title">Happy Customer Reviews</h2>
  <div class="rule"></div>
  <div class="avatar" role="img" aria-label="Customer portrait"></div>
  <div class="quote">
    <span class="mark">“</span>
    <p>Lorem ipsum dolor sit amet, consectetuer adipiscing elit, sed diam nonummy nibh euismod tincidunt ut laoreet dolore magna aliquam erat volutpat. Ut wisi enim ad minim veniam, quis nostrud exerci tation ullamcorper suscipit lobortis nisl ut aliquip commodo consequat. Duis autem vel eum iriure dolor in hendrerit in vulputate velit esse molestie consequat, vel illum dolore eu feugiat nulla facilisis at vero eros et accumsan et iusto odio dignissim qui blandit praesent luptatum.</p>
    <p class="by">— Lorem Ipsum, Manager</p>
  </div>
  <div class="arrows">
    <span><svg width="10" height="10" viewBox="0 0 12 12"><path d="M8 2 4 6l4 4" stroke="#fff" stroke-width="2" fill="none"/></svg></span>
    <span><svg width="10" height="10" viewBox="0 0 12 12"><path d="M4 2l4 4-4 4" stroke="#fff" stroke-width="2" fill="none"/></svg></span>
  </div>
</section>

<section class="why">
  <h2 class="section-title">Why Choose Us</h2>
  <div class="rule"></div>
  <div class="features">
    <div class="feature"><div class="icon active"><svg width="44" height="44" viewBox="0 0 44 44" fill="#fff"><circle cx="16" cy="9" r="5"/><path d="M9 18h14v14h-3v10h-8V32H9z"/><circle cx="31" cy="28" r="9" fill="none" stroke="#fff" stroke-width="2.5"/></svg></div><h4>A PROVEN BROKERAGE</h4></div>
    <div class="feature"><div class="icon"><svg width="48" height="40" viewBox="0 0 48 40" fill="none" stroke="#222" stroke-width="2.5"><rect x="4" y="10" width="36" height="22" rx="2"/><circle cx="22" cy="21" r="6"/><path d="M10 6h34v22"/></svg></div><h4>NO JUNK FEES</h4></div>
    <div class="feature"><div class="icon"><svg width="46" height="40" viewBox="0 0 46 40" fill="none" stroke="#222" stroke-width="2.5"><rect x="3" y="6" width="32" height="22"/><path d="M19 28v6M11 36h16M28 14l14-8v20l-14-6z"/></svg></div><h4>PROFESSIONAL MARKETING</h4></div>
    <div class="feature"><div class="icon"><svg width="40" height="44" viewBox="0 0 40 44" fill="none" stroke="#222" stroke-width="2.5"><path d="M6 3h20l7 7v31H6z"/><path d="M11 14h14M11 20h14M11 26h8M20 36l14-14 4 4-14 14h-4z"/></svg></div><h4>ELECTRONIC SIGNATURES</h4></div>
    <div class="feature"><div class="icon"><svg width="40" height="46" viewBox="0 0 40 46" fill="none" stroke="#222" stroke-width="2.5"><rect x="6" y="3" width="24" height="40" rx="3"/><path d="M14 24l8 8 12-12"/></svg></div><h4>DIGITAL MARKETING EXPERTS</h4></div>
    <div class="feature"><div class="icon"><svg width="46" height="46" viewBox="0 0 46 46" fill="#222"><circle cx="23" cy="23" r="5"/><circle cx="23" cy="6" r="4"/><circle cx="7" cy="18" r="4"/><circle cx="39" cy="18" r="4"/><circle cx="12" cy="38" r="4"/><circle cx="34" cy="38" r="4"/><path d="M23 10v8M11 19l7 3M35 19l-7 3M15 35l5-8M31 35l-5-8" stroke="#222" stroke-width="2"/></svg></div><h4>OUR VENDOR NETWORK</h4></div>
  </div>
</section>

<section class="listings">
  <h2 class="section-title">Featured Listings</h2>
  <div class="rule"></div>
  <div class="cards">
    <div class="card">
      <div class="photo" role="img" aria-label="Two-storey stone house exterior" style="background:linear-gradient(180deg,#a9c3dc,#b7ab98 50%,#6f7b55)"></div>
      <h5>123 Dollar Smit Amet</h5><p class="desc">Duis autem vel eum iriure</p>
      <div class="row"><span class="tag rent">For Rent</span><span class="price">$ 123</span></div>
      <div class="meta"><span>1200 sq ft</span><span>2 Beds</span><span>2 Baths</span></div>
    </div>
    <div class="card">
      <div class="photo" role="img" aria-label="Bright interior with red feature wall" style="background:linear-gradient(180deg,#d8d6d2,#b34a3a 55%,#7d6a55)"></div>
      <h5>123 Dollar Smit Amet</h5><p class="desc">Duis autem vel eum iriure</p>
      <div class="row"><span class="tag sold">Sold</span><span class="price">$ 213</span></div>
      <div class="meta"><span>1200 sq ft</span><span>2 Beds</span><span>2 Baths</span></div>
    </div>
    <div class="card">
      <div class="photo" role="img" aria-label="Open-plan living room with large windows" style="background:linear-gradient(180deg,#e6e3dd,#7fa6b8 50%,#8a6e55)"></div>
      <h5>123 Dollar Smit Amet</h5><p class="desc">Duis autem vel eum iriure</p>
      <div class="row"><span class="tag sold">For Rent</span><span class="price">$ 143</span></div>
      <div class="meta"><span>1200 sq ft</span><span>2 Beds</span><span>2 Baths</span></div>
    </div>
    <div class="card">
      <div class="photo" role="img" aria-label="Grey two-storey house at dusk" style="background:linear-gradient(180deg,#7f98b4,#4b5563 55%,#354030)"></div>
      <h5>123 Dollar Smit Amet</h5><p class="desc">Duis autem vel eum iriure</p>
      <div class="row"><span class="tag sold">For Sell</span><span class="price">$ 132</span></div>
      <div class="meta"><span>1200 sq ft</span><span>2 Beds</span><span>2 Baths</span></div>
    </div>
  </div>
</section>

<section class="newsletter">
  <div class="container">
    <div class="badge"><svg width="22" height="16" viewBox="0 0 22 16" fill="none" stroke="#fff" stroke-width="2"><rect x="1" y="1" width="20" height="14"/><path d="M1 1l10 8 10-8"/></svg></div>
    <h3>Newsletter Signup</h3>
    <svg class="chev" width="16" height="44" viewBox="0 0 16 44"><path d="M2 2l12 20L2 42" stroke="#fff" stroke-width="2" fill="none"/></svg>
    <div class="input">Your e-mail</div>
    <div class="submit">SIGN UP</div>
  </div>
</section>

<footer class="footer">
  <div class="container cols">
    <div class="col" style="left:0">
      <h4>Quick <em>Links</em></h4>
      <ul class="links"><li>Find A Home</li><li>Sell Your Home</li><li>Hearthline Blog</li><li>Our Agents</li><li>Contact Us</li></ul>
    </div>
    <div class="col" style="left:237px">
      <h4>Contact <em>Details</em></h4>
      <div class="info">
        <div><i><svg width="12" height="16" viewBox="0 0 12 16" fill="#fff"><path d="M6 0a6 6 0 0 1 6 6c0 4-6 10-6 10S0 10 0 6a6 6 0 0 1 6-6z"/><circle cx="6" cy="6" r="2" fill="#16a68f"/></svg></i>Street Name, City Name<br>State, Zipcode</div>
        <div><i><svg width="14" height="14" viewBox="0 0 14 14" fill="#fff"><path d="M3 0l3 3-2 2a8 8 0 0 0 5 5l2-2 3 3-2 3C5 14 0 9 0 3z"/></svg></i>123-456-7890 (TF)</div>
        <div><i><svg width="14" height="14" viewBox="0 0 14 14" fill="#fff"><path d="M3 0l3 3-2 2a8 8 0 0 0 5 5l2-2 3 3-2 3C5 14 0 9 0 3z"/></svg></i>123-456-7890</div>
        <div><i><svg width="16" height="12" viewBox="0 0 16 12" fill="none" stroke="#fff" stroke-width="1.6"><rect x="1" y="1" width="14" height="10"/><path d="M1 1l7 6 7-6"/></svg></i>hello@lanterlyhomes.com</div>
      </div>
    </div>
    <div class="col" style="left:584px">
      <h4>Quick <em>Contact</em></h4>
      <div class="form">
        <div>Your name</div><div>Your email</div><div>Your phone number</div><div class="msg">Your message</div>
        <span class="send">SUBMIT</span>
      </div>
    </div>
    <div class="col" style="left:889px">
      <h4>Follow <em>Us</em></h4>
      <div class="follow">
        <div><i></i>PINECAST</div>
        <div><i></i>QUIPSTER</div>
        <div><i></i>LINKWELL</div>
        <div><i></i>ORBITPLUS</div>
      </div>
    </div>
  </div>
</footer>
<div class="copy">Copyright © 2016 Lanterly Homes Collective. All rights reserved.</div>

</body>
</html>
```